New and fresh design template for my Mailwick Studio

This is my current one - http://norvellhomesdanbrisk.sendloop-mail.com/t/ViewEmail/r/C7A4410B2E9D53F61A08CB7E59D24A13

All I need is a new template. I want to keep the same content - New listings, price changes ect however looking to revamp and make it look minimal and sexy - If possible I would like it to adapt to the device it is being seen on.

Target Market(s)

My realestate client database - Buyers, sellers, people wanting to monitor the market

Industry/Entity Type

Real Estate Agent

Font styles to use
Other font styles liked:
• Something clean

Colors
ec1f27
ffffff
000000
5c5c5c

Requirements
Must have
• A similar color scheme - Black, white and red

```html
<!DOCTYPE html>
<html lang="en">
<head>
<meta charset="utf-8">
<title>Norvell Homes – Property Update</title>
<link rel="stylesheet" href="https://fonts.googleapis.com/css2?family=Lato:ital,wght@0,400;0,700;0,900;1,400&family=Oswald:wght@500&display=swap">
<style>
:root{
  --red:#ec1f27;
  --black:#000000;
  --white:#ffffff;
  --grey:#5c5c5c;
  --ink:#333333;
  --line:#d6d6d6;
  --page:#f0f0f0;
  --panel:#f6f6f6;
  --navy:#1f2a44;
}
*{box-sizing:border-box;margin:0;padding:0}
html,body{width:1200px;height:2460px;overflow:hidden}
body{background:var(--page);font-family:'Lato',sans-serif;color:var(--grey);position:relative}
.abs{position:absolute}
.preheader{top:22px;left:0;width:1200px;text-align:center;font-size:19px;color:var(--navy)}
.preheader a,.unsub a{color:var(--red);text-decoration:none;border-bottom:1px solid var(--red)}
.sheet{left:48px;top:68px;width:1102px;height:2310px;background:var(--white);box-shadow:0 0 4px rgba(0,0,0,.15)}
.masthead{left:48px;top:68px;width:1102px;height:108px;background:var(--black)}
.brand{width:80px;height:80px;border:1.5px solid var(--white);border-radius:50%;display:flex;align-items:center;justify-content:center;color:var(--white);font-size:13px;font-weight:700;text-align:center;line-height:1.1}
.social{display:flex;gap:8px}
.social span{width:37px;height:37px;border-radius:50%;background:var(--white);display:block}
.photo-frame{background:var(--white);box-shadow:0 1px 5px rgba(0,0,0,.25)}
.photo-fill{position:absolute}
.headline{left:451px;top:212px;font-size:36px;color:var(--red);font-weight:400;letter-spacing:.5px}
.pill{display:flex;align-items:center;background:var(--black);color:var(--white);border-radius:24px;font-size:17px;font-weight:700;padding-left:25px;position:absolute;overflow:hidden}
.pill::after{content:"";position:absolute;right:0;top:0;width:36px;height:100%;background:var(--red);border-radius:0 24px 24px 50%}
.copy{font-size:16px;line-height:21.6px;color:var(--grey)}
.copy p{margin-bottom:12px}
.spaced{letter-spacing:3px;font-weight:700}
.rule{height:1px;background:var(--line)}
.promo{left:738px;top:634px;width:370px;height:356px;background:radial-gradient(ellipse at 50% 70%,#6b5a48 0%,#2a2520 45%,#050505 80%);color:var(--white);text-align:center}
.promo .t1{margin-top:14px;font-size:18px;letter-spacing:2px}
.promo .t2{font-size:14px;font-weight:900;margin-top:6px}
.promo .t3{font-size:8px}
.promo .t4{font-size:13px;margin-top:4px;letter-spacing:1px}
.promo .t5{position:absolute;bottom:22px;width:100%;font-size:7px;opacity:.8}
.promo .t6{position:absolute;bottom:8px;width:100%;font-size:9px;letter-spacing:1px}
.steps{list-style:none;font-style:italic;margin:4px 0 6px 44px}
.steps li{line-height:24px}
.section-title{font-family:'Oswald',sans-serif;font-weight:500;color:var(--red);font-size:25px;text-transform:uppercase;letter-spacing:-.3px}
.section-title::after{content:"";display:block;width:38px;height:1px;background:var(--line);margin-top:6px}
.centred::after{margin:6px auto 0}
.thumb{width:75px;height:76px;border:2px solid #c7c7c7}
.thumb.active{border-color:var(--red)}
.arrow-btn{width:30px;height:30px}
.listing-title{font-weight:900;color:var(--red);font-size:16px}
.list{list-style:none;font-size:16px;line-height:21.6px;color:var(--grey)}
.now{color:var(--red)}
.vrule{width:1px;background:var(--line)}
.contact{left:542px;top:1916px;width:556px;height:344px;background:var(--panel);border:1px solid #cfcfcf}
.contact-row{font-size:14px;color:var(--black);display:flex;align-items:center;gap:10px}
.tagline{font-size:13px;font-weight:700;color:var(--black);line-height:19px}
.footer{left:46px;top:2280px;width:1102px;height:98px;background:var(--red)}
.footer-tab{left:366px;top:2322px;width:462px;height:56px}
.footer-text{left:366px;top:2338px;width:462px;text-align:center;font-size:15px;font-weight:900;color:#222}
.unsub{top:2414px;left:0;width:1200px;text-align:center;font-size:17px;color:var(--navy)}
</style>
</head>
<body>
<div class="abs preheader">Having Problems viewing this email? <a href="#">Click here</a> to view in browser.</div>

<div class="abs sheet"></div>
<header class="abs masthead">
  <div class="abs brand" style="left:38px;top:13px">Norvell<br>Homes</div>
  <div class="abs social" style="left:919px;top:35px"><span></span><span></span><span></span></div>
</header>

<div class="abs photo-frame" style="left:118px;top:221px;width:315px;height:419px">
  <div class="photo-fill" role="img" aria-label="Portrait of the property consultant in a blue blazer holding plans, ocean view behind" style="left:10px;top:14px;width:294px;height:391px;background:linear-gradient(180deg,#c9d6e2 0%,#9fb6c7 30%,#3e5e8a 60%,#d9dde3 100%)"></div>
</div>

<h1 class="abs headline">2015 MARKET WRAP</h1>
<a class="pill" style="left:628px;top:274px;width:164px;height:42px">CLICK HERE</a>

<div class="abs copy" style="left:496px;top:362px;width:470px">
  <p>Hi ,</p>
  <p>Welcome to the “Property Update”</p>
  <p><span class="spaced">THANK YOU!</span> After a massive quarter I have just taken out the joint number #1 spot. A big shoutout to my supportive and loving wife Claire. I couldn't do it without her</p>
  <p>As always, please let me know if I can assist.</p>
</div>
<div class="abs rule" style="left:496px;top:566px;width:434px"></div>

<div class="abs copy" style="left:188px;top:722px;width:490px">
  <p>Have you got a third wheel? This could be the COMP for you and your TRIO!</p>
  <p style="margin-bottom:2px">To WIN a TRIPLE pass to Sable Creek TRIO Simply</p>
  <ol class="steps">
    <li>1. "Like" Rory Hallett Property</li>
    <li>2. "Share &amp; like" the photo</li>
    <li>3. "Tag" your THIRD wheel</li>
  </ol>
  <p>Winner drawn 22nd of January</p>
</div>
<a class="pill" style="left:187px;top:932px;width:246px;height:45px">CLICK HERE TO ENTER</a>

<div class="abs promo" role="img" aria-label="Promotional photo of the three band members">
  <div class="t1">Win a triple pass to</div>
  <div class="t2">SABLE CREEK TRIO</div>
  <div class="t3">in Elm Bay Park · Summer Day</div>
  <div class="t4">with your trio!</div>
  <div class="t5">with compliments</div>
  <div class="t6">PROPERTY CONSULTANT</div>
</div>

<h2 class="abs section-title centred" style="left:376px;top:1056px;width:400px;text-align:center">Our Latest Listings</h2>

<svg class="abs arrow-btn" style="left:241px;top:1157px" viewBox="0 0 30 30"><circle cx="15" cy="15" r="13.5" fill="none" stroke="#aaa" stroke-width="1.5"/><path d="M17 9l-6 6 6 6" fill="none" stroke="#aaa" stroke-width="1.5"/></svg>
<div class="abs thumb" style="left:298px;top:1134px;background:linear-gradient(180deg,#9db3c8,#8a6a4f)" role="img" aria-label="Timber deck listing"></div>
<div class="abs thumb" style="left:428px;top:1134px;background:linear-gradient(180deg,#b8cde0,#8a9db3 60%,#c7c7c7)" role="img" aria-label="Blue house listing"></div>
<div class="abs thumb" style="left:559px;top:1134px;background:linear-gradient(180deg,#5f8ec4,#9aa9b4 60%,#d6d6d6)" role="img" aria-label="Garage home listing"></div>
<div class="abs thumb active" style="left:689px;top:1134px;background:linear-gradient(180deg,#9aa7b5,#6e8a3e 55%,#8b3a2a)" role="img" aria-label="Brick terrace listing"></div>
<div class="abs thumb" style="left:820px;top:1134px;background:linear-gradient(180deg,#9aa7b5,#6e8a3e 55%,#8b3a2a)" role="img" aria-label="Brick terrace listing"></div>
<svg class="abs arrow-btn" style="left:922px;top:1157px" viewBox="0 0 30 30"><circle cx="15" cy="15" r="13.5" fill="none" stroke="#aaa" stroke-width="1.5"/><path d="M13 9l6 6-6 6" fill="none" stroke="#aaa" stroke-width="1.5"/></svg>
<div class="abs rule" style="left:266px;top:1232px;width:636px"></div>
<div class="abs" style="left:684px;top:1231px;width:91px;height:2px;background:#555"></div>

<div class="abs photo-frame" style="left:299px;top:1274px;width:259px;height:221px">
  <div class="photo-fill" role="img" aria-label="Two-storey red brick terrace with garden and balcony" style="left:9px;top:9px;width:241px;height:203px;background:linear-gradient(180deg,#7f93a8 0%,#a4552f 40%,#5f7a34 75%,#3a2a22 100%)"></div>
</div>
<div class="abs copy" style="left:586px;top:1283px;width:380px">
  <div class="listing-title">79 COLTON STREET, HOBART</div>
  <div style="font-size:14px;color:var(--ink)">FOR SALE: $495,000 - $545,000</div>
  <div style="margin-top:8px;font-weight:700;color:var(--ink);display:flex;align-items:center;gap:6px">
    <svg width="26" height="16" viewBox="0 0 26 16"><rect x="1" y="2" width="17" height="12" fill="none" stroke="#555" stroke-width="1.3"/><path d="M18 8l6-4v8z" fill="none" stroke="#555" stroke-width="1.3"/></svg>VIDEO</div>
  <div style="margin-top:10px;font-style:italic;font-size:15px">4 Bedrooms, 2 Bathroom</div>
  <div style="margin-top:10px;font-size:15px">Iconic 1910's brick home Beautiful character features throughout Within walking distance to the CBD Low maintenance private courtyard Fantastic location, close to everything</div>
</div>

<h2 class="abs section-title" style="left:110px;top:1558px">Upcoming Properties</h2>
<h2 class="abs section-title" style="left:505px;top:1558px">Price Changes</h2>
<h2 class="abs section-title" style="left:838px;top:1558px">Under Offer (Past 7 Days)</h2>

<div class="abs vrule" style="left:462px;top:1606px;height:194px"></div>
<div class="abs vrule" style="left:786px;top:1606px;height:194px"></div>

<ul class="abs list" style="left:124px;top:1616px;width:320px">
  <li style="display:flex;gap:14px;margin-bottom:21px"><svg width="24" height="24" viewBox="0 0 24 24"><circle cx="11" cy="13" r="9" fill="none" stroke="var(--red)" stroke-width="2"/><path d="M6 12l5 5 11-14" fill="none" stroke="var(--red)" stroke-width="2.4"/></svg><span>58 Kestrel Avenue, GEILSTON BAY<br>$335,000 - $365,000</span></li>
  <li style="display:flex;gap:14px;margin-bottom:21px"><svg width="24" height="24" viewBox="0 0 24 24"><circle cx="11" cy="13" r="9" fill="none" stroke="var(--red)" stroke-width="2"/><path d="M6 12l5 5 11-14" fill="none" stroke="var(--red)" stroke-width="2.4"/></svg><span>20 Linden Crescent, OAKDOWNS<br>$395,000 - $435,000</span></li>
  <li style="display:flex;gap:14px"><svg width="24" height="24" viewBox="0 0 24 24"><circle cx="11" cy="13" r="9" fill="none" stroke="var(--red)" stroke-width="2"/><path d="M6 12l5 5 11-14" fill="none" stroke="var(--red)" stroke-width="2.4"/></svg><span>365 Marlow Street, NORTH HOBART<br>$380,000 - $420,000</span></li>
</ul>
<div class="abs" style="left:118px;top:1801px;font-size:15px;color:var(--ink)">*Please note these prices are just a guide</div>

<ul class="abs list" style="left:505px;top:1614px;width:270px">
  <li style="margin-bottom:21px">20 Corbin Place, GEILSTON BAY<br><span class="now">NOW: $365,000 - $395,000</span></li>
  <li style="margin-bottom:21px">2/70 Pelham Road, HOWRAH<br><span class="now">NOW: $395,000</span></li>
  <li>31 Ashby Drive, HOWRAH<br><span class="now">NOW: $385,000 - $415,000</span></li>
</ul>

<ul class="abs list" style="left:838px;top:1616px;width:300px;line-height:36px">
  <li style="display:flex;align-items:center;gap:8px"><svg width="22" height="20" viewBox="0 0 22 20"><path d="M2 10l8-8h9v9l-8 8z" fill="var(--red)"/><circle cx="15" cy="6" r="1.6" fill="#fff"/></svg>12 Wren Court, TRANMERE</li>
  <li style="display:flex;align-items:center;gap:8px"><svg width="22" height="20" viewBox="0 0 22 20"><path d="M2 10l8-8h9v9l-8 8z" fill="var(--red)"/><circle cx="15" cy="6" r="1.6" fill="#fff"/></svg>240 Halden Road, WARRANE</li>
  <li style="display:flex;align-items:center;gap:8px"><svg width="22" height="20" viewBox="0 0 22 20"><path d="M2 10l8-8h9v9l-8 8z" fill="var(--red)"/><circle cx="15" cy="6" r="1.6" fill="#fff"/></svg>8 Fenwick Street, MONTROSE</li>
  <li style="display:flex;align-items:center;gap:8px"><svg width="22" height="20" viewBox="0 0 22 20"><path d="M2 10l8-8h9v9l-8 8z" fill="var(--red)"/><circle cx="15" cy="6" r="1.6" fill="#fff"/></svg>44 Brisco Street, WARRANE</li>
  <li style="display:flex;align-items:center;gap:8px"><svg width="22" height="20" viewBox="0 0 22 20"><path d="M2 10l8-8h9v9l-8 8z" fill="var(--red)"/><circle cx="15" cy="6" r="1.6" fill="#fff"/></svg>55 Tarrow Street, GEILSTON BAY</li>
  <li style="display:flex;align-items:center;gap:8px"><svg width="22" height="20" viewBox="0 0 22 20"><path d="M2 10l8-8h9v9l-8 8z" fill="var(--red)"/><circle cx="15" cy="6" r="1.6" fill="#fff"/></svg>3 Oakley Drive, MONTROSE</li>
</ul>

<div class="abs rule" style="left:126px;top:1860px;width:954px"></div>

<h2 class="abs section-title" style="left:127px;top:1888px">Sold (Past 7 Days)</h2>
<ul class="abs list" style="left:124px;top:1936px;line-height:33.6px">
  <li>5 Ferris Street, SOUTH HOBART $477,650</li>
  <li>84 Carlow Crescent, WEST HOBART $155,000</li>
  <li>31 Heron Street, HOWRAH $450,000</li>
  <li>843 Ridgeway Road, FERN TREE $405,000</li>
  <li>36 Elgin Avenue, WEST MOONAH $420,000</li>
  <li>87 Brantley Road, MIDWAY POINT $130,000</li>
  <li>22a Larch Street, NORTH HOBART $645,000</li>
  <li>1/7 Jasmine Grove, SANDY BAY $530,000</li>
  <li>53 Westbury Crescent, WEST HOBART $360,000</li>
</ul>

<div class="abs contact">
  <div class="abs contact-row" style="left:44px;top:42px"><svg width="26" height="18" viewBox="0 0 26 18"><path d="M2 7c0-4 22-4 22 0v2h-6V6H8v3H2z" fill="#111"/><path d="M6 9h14l3 8H3z" fill="#111"/></svg>0400 123 456</div>
  <div class="abs contact-row" style="left:244px;top:40px"><svg width="18" height="22" viewBox="0 0 18 22"><rect x="2" y="1" width="10" height="17" rx="1.5" fill="none" stroke="#111" stroke-width="2"/><path d="M10 14l6 4-3 3z" fill="#111"/></svg>03 6100 2200</div>
  <div class="abs rule" style="left:44px;top:79px;width:370px;background:#bdbdbd"></div>
  <svg class="abs" style="left:48px;top:112px" width="16" height="22" viewBox="0 0 16 22"><path d="M8 1a7 7 0 0 1 7 7c0 5-7 13-7 13S1 13 1 8a7 7 0 0 1 7-7z" fill="#111"/><circle cx="8" cy="8" r="2.6" fill="var(--panel)"/></svg>
  <div class="abs contact-row" style="left:78px;top:110px;display:block;line-height:21px">Norvell Homes<br>Lindale</div>
  <div class="abs rule" style="left:78px;top:157px;width:92px;background:#ccc"></div>
  <div class="abs contact-row" style="left:78px;top:162px;display:block;line-height:21px">8 Harbourview Drive<br>Lindale TAS 7099</div>
  <div class="abs contact-row" style="left:44px;top:234px"><svg width="22" height="20" viewBox="0 0 22 20"><rect x="5" y="1" width="12" height="7" fill="#111"/><rect x="1" y="7" width="20" height="9" rx="2" fill="#111"/><rect x="5" y="13" width="12" height="6" fill="#111"/></svg>fax: 03 6100 2211</div>
  <div class="abs" role="img" aria-label="Round portrait of the property consultant" style="left:278px;top:107px;width:148px;height:148px;border-radius:50%;background:radial-gradient(circle at 50% 45%,#8a8580,#3a3a3a 80%)"></div>
  <div class="abs tagline" style="left:79px;top:290px">Trasmania's Largest Independently-Owned Real Estate Company<br>Servicing Southern Tasmania With Offices Across Greater Hobart</div>
</div>

<footer class="abs footer">
  <div class="abs brand" style="left:74px;top:8px">Norvell<br>Homes</div>
  <div class="abs social" style="left:876px;top:35px;gap:8px"><span></span><span></span><span></span></div>
</footer>
<svg class="abs footer-tab" viewBox="0 0 462 56" preserveAspectRatio="none"><path d="M0 56 L28 8 Q32 0 42 0 H420 Q430 0 434 8 L462 56 Z" fill="var(--white)"/></svg>
<div class="abs footer-text">@COPYRIGHT BY NORVELL HOMES COMPANY LIMITED.</div>

<div class="abs unsub">You are receiving this email because you subcribed at www.mailwick.example. To unsubscribe, <a href="#">click here</a></div>
</body>
</html>
```